Consulting firm needs an infographic

The consulting we do needs a very graphic and understandable way to have perspective clients get exactly where we can help their company grow. I designed something that needs a lot of spice for it to look professional and relatable to them. This is being created to be used on a business card, as well as on posters, and social media.

```html
<!DOCTYPE html>
<html lang="en">
<head>
<meta charset="utf-8">
<title>Consulting Growth Map</title>
<link rel="stylesheet" href="https://fonts.googleapis.com/css2?family=Montserrat:wght@400;600;700;800&display=swap">
<style>
  :root {
    --bg-light: #f5f0e7;
    --bg-edge: #e5dbc9;
    --ring: #cfcfcf;
    --track: #ccd3e0;
    --dash: #bfc9da;
    --ink: #4a4a4a;
    --ink-dark: #111111;
    --yellow: #f5b90d;
    --magenta: #d6267d;
    --teal: #16b3c9;
    --green: #8ebf2a;
    --orange: #ea7f35;
    --blue: #4c78c8;
    --arrow-red: #ff2a10;
    --white: #ffffff;
  }
  html, body {
    margin: 0;
    width: 1200px;
    height: 1200px;
    overflow: hidden;
    background: var(--bg-edge);
  }
  .infographic {
    display: block;
    width: 1200px;
    height: 1200px;
    font-family: 'Montserrat', sans-serif;
  }
  .label { font-family: 'Montserrat', sans-serif; font-weight: 700; font-size: 17px; fill: var(--ink); text-anchor: middle; }
  .label-small { font-size: 15px; }
  .sub-label { font-family: 'Montserrat', sans-serif; font-weight: 600; font-size: 6px; fill: var(--ink); text-anchor: end; }
  .hub-title { font-family: 'Montserrat', sans-serif; font-weight: 400; fill: var(--ink); text-anchor: middle; }
  .hub-sub { font-family: 'Montserrat', sans-serif; font-weight: 400; font-size: 18px; letter-spacing: 2.5px; fill: var(--ink); text-anchor: middle; }
  .tab-label { font-family: 'Montserrat', sans-serif; font-weight: 700; font-size: 15px; fill: var(--ink); text-anchor: middle; }
  .brand-name { font-family: 'Montserrat', sans-serif; font-weight: 700; font-size: 24px; fill: var(--ink); }
  .font-note { font-family: 'Montserrat', sans-serif; font-weight: 700; font-size: 30px; fill: var(--ink-dark); text-anchor: end; letter-spacing: -1px; }
  .ring-outer { fill: none; stroke: var(--ring); stroke-width: 7; }
  .ring-dash { fill: none; stroke: var(--dash); stroke-width: 3; stroke-dasharray: 3 7; }
  .track { fill: var(--track); }
  .pill-base { fill: var(--white); filter: url(#soft-shadow); }
  .pill-cover { fill: var(--white); }
  .icon-disc { fill: var(--white); stroke: #d8d8d8; stroke-width: 2; filter: url(#soft-shadow); }
  .icon-line { fill: none; stroke: #666; stroke-width: 2; stroke-linecap: round; stroke-linejoin: round; }
  .node-ring { fill: var(--white); stroke: #d9d9d9; stroke-width: 2; filter: url(#soft-shadow); }
  .dot-yellow { fill: var(--yellow); }
  .dot-magenta { fill: var(--magenta); }
  .dot-teal { fill: var(--teal); }
  .arrow-band { fill: none; stroke: url(#arrow-grey); stroke-width: 58; }
  .arrow-edge { fill: none; stroke: var(--arrow-red); stroke-width: 5; }
  .arrow-head { fill: url(#arrow-grey); stroke: var(--arrow-red); stroke-width: 4; stroke-linejoin: miter; }
</style>
</head>
<body>
<svg class="infographic" viewBox="0 0 1932 1932" xmlns="http://www.w3.org/2000/svg" role="img" aria-label="Consulting growth cycle: company, suppliers, operations and customers">
  <defs>
    <radialGradient id="backdrop" cx="50%" cy="50%" r="70%">
      <stop offset="0" stop-color="#f6f2ea"/>
      <stop offset="1" stop-color="#e4d9c6"/>
    </radialGradient>
    <linearGradient id="hub-green" x1="0" y1="0" x2="1" y2="1">
      <stop offset="0" stop-color="#dcebc8"/>
      <stop offset="1" stop-color="#a9d48b"/>
    </linearGradient>
    <linearGradient id="g-yellow" x1="0" x2="1"><stop offset="0" stop-color="#f39a08"/><stop offset="1" stop-color="#fbd71e"/></linearGradient>
    <linearGradient id="g-magenta" x1="0" x2="1"><stop offset="0" stop-color="#b81a6c"/><stop offset="1" stop-color="#f23e98"/></linearGradient>
    <linearGradient id="g-teal" x1="0" x2="1"><stop offset="0" stop-color="#0d8fbe"/><stop offset="1" stop-color="#1ad4d6"/></linearGradient>
    <linearGradient id="g-green" x1="0" x2="1"><stop offset="0" stop-color="#5f9a1c"/><stop offset="1" stop-color="#a8cf2c"/></linearGradient>
    <linearGradient id="half-yellow-l" x1="0" x2="1"><stop offset="0" stop-color="#e8c96a"/><stop offset="1" stop-color="#f6b915"/></linearGradient>
    <linearGradient id="half-yellow-r" x1="0" x2="1"><stop offset="0" stop-color="#f6b915"/><stop offset="1" stop-color="#e8c96a"/></linearGradient>
    <linearGradient id="half-blue-l" x1="0" x2="1"><stop offset="0" stop-color="#7fa0da"/><stop offset="1" stop-color="#3f6cc4"/></linearGradient>
    <linearGradient id="half-blue-r" x1="0" x2="1"><stop offset="0" stop-color="#3f6cc4"/><stop offset="1" stop-color="#7fa0da"/></linearGradient>
    <linearGradient id="half-orange-l" x1="0" x2="1"><stop offset="0" stop-color="#e3a57f"/><stop offset="1" stop-color="#ea7a2e"/></linearGradient>
    <linearGradient id="half-orange-r" x1="0" x2="1"><stop offset="0" stop-color="#ea7a2e"/><stop offset="1" stop-color="#e3a57f"/></linearGradient>
    <linearGradient id="arrow-grey" x1="0" y1="0" x2="1" y2="1">
      <stop offset="0" stop-color="#7d7d7d"/>
      <stop offset="0.5" stop-color="#b5b5b5"/>
      <stop offset="1" stop-color="#7a7a7a"/>
    </linearGradient>
    <linearGradient id="tab-white" x1="0" x2="1"><stop offset="0" stop-color="#e2e2e2"/><stop offset="0.5" stop-color="#ffffff"/><stop offset="1" stop-color="#e2e2e2"/></linearGradient>
    <filter id="soft-shadow" x="-20%" y="-30%" width="140%" height="170%">
      <feDropShadow dx="0" dy="5" stdDeviation="5" flood-color="#000" flood-opacity="0.22"/>
    </filter>
  </defs>

  <rect class="backdrop" width="1932" height="1932" fill="url(#backdrop)"/>

  <!-- Flow arrows -->
  <g class="flow-arrow">
    <path class="arrow-band" d="M755,550 L535,550 Q470,550 470,615 L470,660"/>
    <path class="arrow-edge" d="M755,579 L535,579 Q499,579 499,615 L499,660"/>
    <polygon class="arrow-head" points="420,656 522,656 470,746"/>
  </g>
  <g class="flow-arrow">
    <path class="arrow-band" d="M1532,748 L1532,625 Q1532,562 1470,562 L1282,562"/>
    <path class="arrow-edge" d="M1503,748 L1503,625 Q1503,591 1470,591 L1282,591"/>
    <polygon class="arrow-head" points="1284,512 1284,612 1190,562"/>
  </g>
  <g class="flow-arrow">
    <path class="arrow-band" d="M458,1162 L460,1300 Q465,1365 530,1365"/>
    <path class="arrow-edge" d="M487,1162 L489,1300 Q492,1336 525,1336"/>
    <polygon class="arrow-head" points="522,1297 522,1398 612,1347"/>
  </g>
  <g class="flow-arrow">
    <path class="arrow-band" d="M1332,1368 L1450,1368 Q1518,1368 1518,1300 L1518,1262"/>
    <path class="arrow-edge" d="M1332,1339 L1450,1339 Q1489,1339 1489,1300 L1489,1262"/>
    <polygon class="arrow-head" points="1467,1262 1568,1262 1517,1172"/>
  </g>

  <!-- Hub: company -->
  <g class="hub">
    <circle class="ring-outer" cx="975" cy="615" r="230"/>
    <circle cx="975" cy="615" r="186" fill="#e6e6e9"/>
    <circle cx="973" cy="612" r="143" fill="url(#hub-green)" filter="url(#soft-shadow)"/>
    <text class="hub-title" x="966" y="574" font-size="46">YOUR</text>
    <text class="hub-title" x="975" y="630" font-size="50">COMPANY</text>
    <text class="hub-sub" x="974" y="653">PRODUCT /SERVICES</text>

    <rect x="843" y="694" width="260" height="22" rx="11" fill="#d6d6d6"/>
    <rect x="850" y="700" width="80" height="10" rx="5" class="dot-teal"/>
    <rect x="930" y="700" width="82" height="10" class="dot-magenta"/>
    <rect x="1012" y="700" width="82" height="10" rx="5" class="dot-yellow"/>

    <g class="hub-tab">
      <rect x="863" y="742" width="58" height="205" rx="29" fill="url(#tab-white)" filter="url(#soft-shadow)"/>
      <path d="M869,860 L892,882 L915,860 L915,915 A23,23 0 0 1 869,915 Z" fill="url(#g-teal)"/>
      <circle class="node-ring" cx="892" cy="705" r="15"/><circle class="dot-teal" cx="892" cy="705" r="8"/>
      <circle class="icon-disc" cx="892" cy="914" r="19"/>
      <path class="icon-line" d="M885,906 h10 v16 h-10 z M888,911 h4 M888,915 h4"/>
      <text class="tab-label" transform="translate(887,808) rotate(90)">WORKFORCE</text>
    </g>
    <g class="hub-tab">
      <rect x="945" y="742" width="58" height="205" rx="29" fill="url(#tab-white)" filter="url(#soft-shadow)"/>
      <path d="M951,860 L974,882 L997,860 L997,915 A23,23 0 0 1 951,915 Z" fill="url(#g-magenta)"/>
      <circle class="node-ring" cx="974" cy="705" r="15"/><circle class="dot-magenta" cx="974" cy="705" r="8"/>
      <circle class="icon-disc" cx="974" cy="914" r="19"/>
      <circle class="icon-line" cx="974" cy="915" r="8"/><circle class="icon-line" cx="974" cy="915" r="3"/>
      <text class="tab-label" transform="translate(969,808) rotate(90)">WORKPLACE</text>
    </g>
    <g class="hub-tab">
      <rect x="1022" y="742" width="58" height="205" rx="29" fill="url(#tab-white)" filter="url(#soft-shadow)"/>
      <path d="M1028,860 L1051,882 L1074,860 L1074,915 A23,23 0 0 1 1028,915 Z" fill="url(#g-yellow)"/>
      <circle class="node-ring" cx="1051" cy="705" r="15"/><circle class="dot-yellow" cx="1051" cy="705" r="8"/>
      <circle class="icon-disc" cx="1051" cy="914" r="19"/>
      <path class="icon-line" d="M1044,907 L1058,921 M1058,907 L1044,921"/>
      <text class="tab-label" transform="translate(1046,808) rotate(90)">WORKFLOW</text>
    </g>
  </g>

  <!-- Brand name -->
  <g class="brand">
    <circle cx="857" cy="1065" r="13" fill="var(--magenta)"/>
    <text class="brand-name" x="880" y="1074">Norvale Advisory</text>
  </g>

  <!-- Module: suppliers (left) -->
  <g class="module module-suppliers">
    <rect class="ring-outer" x="30" y="742" width="762" height="434" rx="217"/>
    <rect class="ring-dash" x="56" y="768" width="710" height="380" rx="190"/>
    <rect class="track" x="78" y="790" width="664" height="336" rx="168"/>
    <path d="M245,808 A148.5,148.5 0 0 0 245,1105 Z" fill="url(#half-yellow-l)"/>
    <path d="M576,808 A148.5,148.5 0 0 1 576,1105 Z" fill="url(#half-yellow-r)"/>
    <circle class="dot-yellow" cx="208" cy="918" r="10"/><circle class="dot-magenta" cx="208" cy="952" r="10"/><circle class="dot-teal" cx="208" cy="986" r="10"/>
    <circle class="dot-yellow" cx="626" cy="918" r="10"/><circle class="dot-magenta" cx="626" cy="952" r="10"/><circle class="dot-teal" cx="626" cy="986" r="10"/>
    <rect x="270" y="826" width="22" height="256" rx="11" fill="#e3e6ec"/>
    <rect x="276" y="832" width="10" height="82" class="dot-yellow"/><rect x="276" y="914" width="10" height="82" class="dot-magenta"/><rect x="276" y="996" width="10" height="80" class="dot-teal"/>

    <g transform="translate(322,848)">
      <rect class="pill-base" width="230" height="52" rx="26"/>
      <rect x="100" width="130" height="52" rx="26" fill="url(#g-yellow)"/>
      <path class="pill-cover" d="M26,0 H118 L137,26 L118,52 H26 A26,26 0 0 1 26,0 Z"/>
      <text class="label" x="62" y="32">VENDORS</text>
      <circle class="icon-disc" cx="216" cy="26" r="21"/>
      <path class="icon-line" d="M205,26 l6,-5 h10 l6,5 M210,27 l5,4 l4,-3"/>
    </g>
    <g transform="translate(322,926)">
      <rect class="pill-base" width="230" height="52" rx="26"/>
      <rect x="100" width="130" height="52" rx="26" fill="url(#g-magenta)"/>
      <path class="pill-cover" d="M26,0 H118 L137,26 L118,52 H26 A26,26 0 0 1 26,0 Z"/>
      <text class="label" x="68" y="32">RESOURCES</text>
      <circle class="icon-disc" cx="216" cy="26" r="21"/>
      <circle class="icon-line" cx="216" cy="26" r="8"/><circle class="icon-line" cx="216" cy="26" r="3"/>
    </g>
    <g transform="translate(322,1007)">
      <rect class="pill-base" width="230" height="52" rx="26"/>
      <rect x="100" width="130" height="52" rx="26" fill="url(#g-teal)"/>
      <path class="pill-cover" d="M26,0 H118 L137,26 L118,52 H26 A26,26 0 0 1 26,0 Z"/>
      <text class="label" x="61" y="32">COSTS</text>
      <circle class="icon-disc" cx="212" cy="26" r="21"/>
      <circle class="icon-line" cx="212" cy="22" r="6"/><path class="icon-line" d="M202,32 h20"/>
    </g>

    <circle class="node-ring" cx="281" cy="874" r="16"/><circle class="dot-yellow" cx="281" cy="874" r="9"/>
    <circle class="node-ring" cx="281" cy="952" r="16"/><circle class="dot-magenta" cx="281" cy="952" r="9"/>
    <circle class="node-ring" cx="281" cy="1033" r="16"/><circle class="dot-teal" cx="281" cy="1033" r="9"/>
  </g>

  <!-- Module: market (right) -->
  <g class="module module-market">
    <rect class="ring-outer" x="1150" y="740" width="762" height="434" rx="217"/>
    <rect class="ring-dash" x="1176" y="764" width="710" height="380" rx="190"/>
    <rect class="track" x="1198" y="786" width="664" height="336" rx="168"/>
    <path d="M1365,805 A148.5,148.5 0 0 0 1365,1102 Z" fill="url(#half-blue-l)"/>
    <path d="M1696,805 A148.5,148.5 0 0 1 1696,1102 Z" fill="url(#half-blue-r)"/>
    <circle class="dot-yellow" cx="1328" cy="915" r="10"/><circle class="dot-magenta" cx="1328" cy="948" r="10"/><circle class="dot-teal" cx="1328" cy="983" r="10"/>
    <circle class="dot-yellow" cx="1746" cy="915" r="10"/><circle class="dot-magenta" cx="1746" cy="948" r="10"/><circle class="dot-teal" cx="1746" cy="983" r="10"/>
    <rect x="1389" y="822" width="22" height="256" rx="11" fill="#e3e6ec"/>
    <rect x="1395" y="828" width="10" height="82" class="dot-yellow"/><rect x="1395" y="910" width="10" height="82" class="dot-magenta"/><rect x="1395" y="992" width="10" height="80" class="dot-teal"/>

    <g transform="translate(1442,844)">
      <rect class="pill-base" width="230" height="52" rx="26"/>
      <rect x="100" width="130" height="52" rx="26" fill="url(#g-yellow)"/>
      <path class="pill-cover" d="M26,0 H118 L137,26 L118,52 H26 A26,26 0 0 1 26,0 Z"/>
      <text class="label" x="66" y="32">CUSTOMERS</text>
      <circle class="icon-disc" cx="216" cy="26" r="21"/>
      <circle class="icon-line" cx="210" cy="22" r="4"/><circle class="icon-line" cx="222" cy="22" r="4"/><path class="icon-line" d="M204,34 q6,-8 12,0 q6,-8 12,0"/>
    </g>
    <g transform="translate(1442,922)">
      <rect class="pill-base" width="230" height="52" rx="26"/>
      <rect x="100" width="130" height="52" rx="26" fill="url(#g-magenta)"/>
      <path class="pill-cover" d="M26,0 H118 L137,26 L118,52 H26 A26,26 0 0 1 26,0 Z"/>
      <text class="label label-small" x="66" y="31">IDENTITY &amp; B&amp;M</text>
      <text class="sub-label" x="126" y="39">Brick and Mortar</text>
      <circle class="icon-disc" cx="214" cy="26" r="21"/>
      <path class="icon-line" d="M209,34 v-10 a5,5 0 0 1 10,0 v10 M214,32 v-8"/>
    </g>
    <g transform="translate(1442,1004)">
      <rect class="pill-base" width="230" height="52" rx="26"/>
      <rect x="100" width="130" height="52" rx="26" fill="url(#g-teal)"/>
      <path class="pill-cover" d="M26,0 H118 L137,26 L118,52 H26 A26,26 0 0 1 26,0 Z"/>
      <text class="label" x="58" y="32">REVENUE</text>
      <circle class="icon-disc" cx="212" cy="26" r="21"/>
    </g>

    <circle class="node-ring" cx="1400" cy="870" r="16"/><circle class="dot-yellow" cx="1400" cy="870" r="9"/>
    <circle class="node-ring" cx="1400" cy="948" r="16"/><circle class="dot-magenta" cx="1400" cy="948" r="9"/>
    <circle class="node-ring" cx="1400" cy="1030" r="16"/><circle class="dot-teal" cx="1400" cy="1030" r="9"/>
  </g>

  <!-- Module: operations (bottom) -->
  <g class="module module-operations">
    <rect class="ring-outer" x="594" y="1172" width="762" height="434" rx="217"/>
    <rect class="ring-dash" x="620" y="1198" width="710" height="380" rx="190"/>
    <rect class="track" x="642" y="1220" width="664" height="336" rx="168"/>
    <path d="M810,1240 A148.5,148.5 0 0 0 810,1537 Z" fill="url(#half-orange-l)"/>
    <path d="M1140,1240 A148.5,148.5 0 0 1 1140,1537 Z" fill="url(#half-orange-r)"/>
    <circle class="dot-yellow" cx="773" cy="1350" r="10"/><circle class="dot-magenta" cx="773" cy="1384" r="10"/><circle class="dot-teal" cx="773" cy="1418" r="10"/>
    <circle class="dot-yellow" cx="1190" cy="1350" r="10"/><circle class="dot-magenta" cx="1190" cy="1384" r="10"/><circle class="dot-teal" cx="1190" cy="1418" r="10"/>
    <rect x="834" y="1258" width="22" height="256" rx="11" fill="#e3e6ec"/>
    <rect x="840" y="1264" width="10" height="82" class="dot-yellow"/><rect x="840" y="1346" width="10" height="82" class="dot-magenta"/><rect x="840" y="1428" width="10" height="80" class="dot-teal"/>

    <path d="M862,1292 L880,1248 H942" fill="none" stroke="var(--green)" stroke-width="2"/>
    <polygon points="946,1248 938,1243 938,1253" fill="var(--green)"/>

    <g transform="translate(965,1228)">
      <rect class="pill-base" width="132" height="36" rx="18"/>
      <rect x="86" width="46" height="36" rx="18" fill="url(#g-green)"/>
      <path class="pill-cover" d="M18,0 H104 L116,18 L104,36 H18 A18,18 0 0 1 18,0 Z"/>
      <text class="label label-small" x="57" y="24">EXECUTIVE</text>
      <circle class="icon-disc" cx="143" cy="18" r="15"/>
      <circle class="icon-line" cx="143" cy="14" r="3"/><path class="icon-line" d="M137,25 q6,-8 12,0"/>
    </g>
    <g transform="translate(888,1280)">
      <rect class="pill-base" width="232" height="52" rx="26"/>
      <rect x="100" width="132" height="52" rx="26" fill="url(#g-yellow)"/>
      <path class="pill-cover" d="M26,0 H130 L148,26 L130,52 H26 A26,26 0 0 1 26,0 Z"/>
      <text class="label label-small" x="74" y="32">ADMINISTRATIVE</text>
      <circle class="icon-disc" cx="215" cy="26" r="21"/>
      <circle class="icon-line" cx="212" cy="22" r="5"/><path class="icon-line" d="M203,35 q9,-10 18,0"/>
    </g>
    <g transform="translate(888,1358)">
      <rect class="pill-base" width="232" height="52" rx="26"/>
      <rect x="100" width="132" height="52" rx="26" fill="url(#g-magenta)"/>
      <path class="pill-cover" d="M26,0 H118 L137,26 L118,52 H26 A26,26 0 0 1 26,0 Z"/>
      <text class="label" x="67" y="32">PERSONNEL</text>
      <circle class="icon-disc" cx="214" cy="26" r="21"/>
      <circle class="icon-line" cx="208" cy="22" r="4"/><circle class="icon-line" cx="220" cy="22" r="4"/><path class="icon-line" d="M202,34 q6,-8 12,0 q6,-8 12,0"/>
    </g>
    <g transform="translate(888,1440)">
      <rect class="pill-base" width="232" height="52" rx="26"/>
      <rect x="100" width="132" height="52" rx="26" fill="url(#g-teal)"/>
      <path class="pill-cover" d="M26,0 H118 L137,26 L118,52 H26 A26,26 0 0 1 26,0 Z"/>
      <text class="label" x="61" y="32">LOGISTICS</text>
      <circle class="icon-disc" cx="211" cy="26" r="21"/>
      <path class="icon-line" d="M202,16 h4 v16 h14 M209,20 h10 v8 h-10 z"/>
    </g>

    <circle class="node-ring" cx="845" cy="1306" r="16"/><circle class="dot-yellow" cx="845" cy="1306" r="9"/>
    <circle class="node-ring" cx="845" cy="1384" r="16"/><circle class="dot-magenta" cx="845" cy="1384" r="9"/>
    <circle class="node-ring" cx="845" cy="1466" r="16"/><circle class="dot-teal" cx="845" cy="1466" r="9"/>
  </g>

  <text class="font-note" x="1912" y="1903">Font: Montserrat</text>
</svg>
</body>
</html>
```